NURSING: RISING PAST THE SHADOWED SILL

Size of the book cover: 140 x 215 mms

I need a cover for the 30,000 word book I have just written. It is a positive take on what I think nursing is and what it needs to be in the future. It is also my story of being nursed and of being a nurse.

My dream is that nurses honor themselves; that they look to the future with confidence and intelligence and that care continues to be delivered with compassionate person centeredness.

I define nursing as a professional workforce which, with probity, prevent or relieve distress; provide compassionate, safe, excellent care; and which contributes to the organization of healthcare.

The name comes from a Biblical parable Corlan 3:7-9. If a light is hidden under a bushel (basket) it is barely seen. If it is lit out from the basket it is clearly seen. As nurses we must continue to take up our mantel and ensure our light is seen and that it continues to shine the way we want it to.

As nurses we each take up our own lantern of caring, each in our own ways. To walk more brightly in our own paths of service.

The final design should show the specialness of nursing.

Target Market(s)

Nurses present, past and future

Industry/Entity Type

Healthcare

Font styles to use
Sans Serif
Other font styles liked:
• Whatever you think will suit

Colors
ec1f27
0393ce
9bcb3c

Requirements
Must have
• Be friendly, calming.
• NB: I am not sure whether the title should be in uppercase or not. Nursing could be uppercase and rising past the shadowed sill could be lower case. I leave it to you experienced people
Nice to have
• Something that depicts nursing...or is suggestive of nursing and the specialness of the work we do. How we bring our light to our patients as we 'hold them in the palms of out hands' and care for them. How they honor us by allowing us into their lives. Our rich past and out history allows us to be who we are today and we look to the future with confidence and hope
• I like rich colors, eg the color type you might find on a stained glass window in a church - rich emerald green or rich crimson red or the deep blue of a nurses cape
Should not have
• A dark cover
• clutter
• Religious overtone
• I have chosen three colors but they are not in the shading I would like - see above

```html
<!DOCTYPE html>
<html lang="en">
<head>
<meta charset="utf-8">
<title>Nursing: Rising Past the Shadowed Sill — Book Cover</title>
<link rel="stylesheet" href="https://fonts.googleapis.com/css2?family=Mulish:wght@300;700;800&family=Arimo&display=swap">
<style>
  :root {
    --cover-red: #ec1f27;
    --cape-blue: #0393ce;
    --ink: #111111;
    --paper: #ffffff;
  }
  html, body {
    margin: 0;
    padding: 0;
    width: 776px;
    height: 1200px;
    overflow: hidden;
    background: var(--paper);
  }
  .book-cover {
    display: block;
    width: 776px;
    height: 1200px;
  }
  .red-shape { fill: var(--cover-red); }
  .author-name {
    font-family: "Mulish", sans-serif;
    font-weight: 800;
    font-size: 60px;
    fill: var(--ink);
  }
  .title-main {
    font-family: "Mulish", sans-serif;
    font-weight: 800;
    font-size: 166px;
    fill: var(--cape-blue);
    letter-spacing: -2px;
  }
  .title-sub {
    font-family: "Mulish", sans-serif;
    font-weight: 300;
    font-size: 35px;
    fill: var(--ink);
  }
  .epigraph {
    font-family: "Arimo", sans-serif;
    fill: var(--ink);
  }
  .epigraph-line-1 { font-size: 15px; }
  .epigraph-line-2 { font-size: 17px; }
  .epigraph-line-3 { font-size: 18.5px; }
</style>
</head>
<body>
  <svg class="book-cover" viewBox="0 0 776 1200" xmlns="http://www.w3.org/2000/svg" role="img" aria-label="Book cover: Nursing, rising past the shadowed sill, by Morven Achery">
    <rect width="776" height="1200" fill="var(--paper)"/>

    <!-- Cross-shaped header: band with stem -->
    <rect class="red-shape header-band" x="0" y="0" width="776" height="134"/>
    <rect class="red-shape header-stem" x="250" y="133" width="270" height="256"/>

    <text class="author-name" x="388" y="93" text-anchor="middle" textLength="501" lengthAdjust="spacingAndGlyphs">Morven Achery</text>

    <!-- Title -->
    <text class="title-main" x="72" y="605" textLength="616" lengthAdjust="spacingAndGlyphs">nursing</text>
    <text class="title-sub" x="74" y="663">rising past the shadowed sill</text>

    <!-- Arched bands -->
    <path class="red-shape arch-wide" d="M0,752 Q388,664 776,752 L776,841 Q388,743 0,841 Z"/>
    <path class="red-shape arch-thin" d="M0,849 Q388,766 776,849 L776,862 Q388,779 0,862 Z"/>
    <path class="red-shape arch-thin" d="M0,871 Q388,788 776,871 L776,890 Q388,808 0,890 Z"/>

    <!-- Epigraph -->
    <text class="epigraph epigraph-line-1" x="187" y="953">“We each take up our own lantern of caring,</text>
    <text class="epigraph epigraph-line-2" x="376" y="978">each in our own ways,</text>
    <text class="epigraph epigraph-line-3" x="162" y="998">to walk more brightly in our own path of service”</text>
  </svg>
</body>
</html>
```